Need Business cards

Im a new realtor and already have a logo. I would like to purchase a Business card design that catches customer's attention, its creative, and modern.

Marisol Quintero
Realtor ®
(555) 318 4027
marisolqtrhomes@brindlemail.com

Target Market(s)

investors, buyers and seller, property management

Industry/Entity Type

real estate,

Contact Information for Business Card

Marisol Quintero

Requirements
Must have
• BOTH LOGOS, WOULD LIKE TO SEE WITH DIFFERENT OPTIONS WITH EITHER PICTURE

```html
<!DOCTYPE html>
<html lang="en">
<head>
<meta charset="utf-8">
<title>Marisol Quintero – Realtor Business Cards</title>
<link href="https://fonts.googleapis.com/css2?family=Montserrat:wght@500;700&family=Roboto+Condensed:wght@400;700&display=swap" rel="stylesheet">
<style>
  :root {
    --backdrop: #ececec;
    --card: #ffffff;
    --gold: #b8892a;
    --gold-light: #d4aa3c;
    --ink: #121212;
    --grey-text: #6b6b6b;
    --broker-blue: #3f6fc2;
    --photo-light: #f3f1f2;
    --photo-mid: #e4dcd6;
  }
  * { margin: 0; padding: 0; box-sizing: border-box; }
  html, body {
    width: 1200px; height: 1041px; overflow: hidden;
    background: var(--backdrop);
  }
  .sheet { position: relative; width: 1200px; height: 1041px; }
  .card {
    position: absolute; top: 153px;
    width: 388px; height: 700px;
    background: var(--card);
    overflow: hidden;
  }
  .card--front { left: 163px; }
  .card--back { left: 648px; }

  /* Front */
  .portrait {
    position: absolute; left: 0; top: 0; width: 388px; height: 600px;
    background:
      radial-gradient(ellipse 42% 48% at 50% 46%, #c9a77e 0%, rgba(201,167,126,0) 70%),
      radial-gradient(ellipse 50% 28% at 52% 62%, #1b1b1b 0%, rgba(27,27,27,0) 75%),
      linear-gradient(180deg, var(--photo-light) 0%, var(--photo-mid) 60%, #f7f7f7 80%, #ffffff 100%);
  }
  .name-band {
    position: absolute; left: 0; bottom: 0; width: 388px; height: 100px;
    background: var(--ink);
    text-align: center; padding-top: 25px;
  }
  .name-band .agent-name {
    font-family: 'Montserrat', sans-serif; font-weight: 700;
    font-size: 21px; color: var(--gold); letter-spacing: 0.2px;
  }
  .name-band .agent-title {
    font-family: 'Roboto Condensed', sans-serif; font-weight: 700;
    font-size: 19px; color: #ffffff; margin-top: 2px;
  }
  sup { font-size: 0.45em; vertical-align: 1.1em; margin-left: 2px; font-weight: 400; }

  /* Back */
  .brand-mark {
    position: absolute; left: 0; top: 150px; width: 388px; text-align: center;
    font-family: 'Montserrat', sans-serif; font-weight: 500; color: var(--gold-light);
  }
  .brand-mark .brand-name { font-size: 20px; letter-spacing: 0.3px; }
  .brand-mark .brand-role { font-size: 13px; letter-spacing: 0.5px; margin-top: 6px; }

  .contact-block { position: absolute; left: 56px; top: 418px; }
  .contact-block .agent-name {
    font-family: 'Montserrat', sans-serif; font-weight: 700;
    font-size: 22px; color: var(--gold); letter-spacing: 0.1px;
  }
  .contact-block .agent-title {
    font-family: 'Roboto Condensed', sans-serif; font-weight: 700;
    font-size: 21px; color: var(--grey-text); margin-top: 2px;
  }
  .contact-list { list-style: none; margin-top: 46px; }
  .contact-list li {
    display: flex; align-items: center; gap: 7px;
    font-family: 'Roboto Condensed', sans-serif; font-weight: 400;
    font-size: 19px; color: var(--grey-text); line-height: 29px;
  }
  .contact-list svg { width: 18px; height: 16px; flex: none; }

  .brokerage {
    position: absolute; left: 0; top: 618px; width: 388px; text-align: center;
    font-family: 'Montserrat', sans-serif; font-weight: 700;
    font-size: 20px; color: var(--broker-blue); letter-spacing: 1px;
  }
</style>
</head>
<body>
<main class="sheet">
  <section class="card card--front">
    <div class="portrait" role="img" aria-label="Portrait photo of the realtor seated at a white table, wearing a black top, against a light studio backdrop"></div>
    <div class="name-band">
      <div class="agent-name">MARISOL QUINTERO</div>
      <div class="agent-title">Realtor<sup>®</sup></div>
    </div>
  </section>

  <section class="card card--back">
    <div class="brand-mark">
      <div class="brand-name">MARISOL QUINTERO</div>
      <div class="brand-role">REALTOR</div>
    </div>

    <div class="contact-block">
      <div class="agent-name">MARISOL QUINTERO</div>
      <div class="agent-title">Realtor<sup>®</sup></div>
      <ul class="contact-list">
        <li>
          <svg viewBox="0 0 18 16" aria-hidden="true">
            <path d="M1 5 Q9 -1 17 5 L15 7 L12 5.5 L12 4 Q9 3 6 4 L6 5.5 L3 7 Z" fill="var(--gold-light)"/>
            <path d="M4 8 L14 8 L16 15 L2 15 Z" fill="var(--gold-light)"/>
            <circle cx="9" cy="11.5" r="2" fill="#fff"/>
          </svg>
          (555) 318 4027
        </li>
        <li>
          <svg viewBox="0 0 18 16" aria-hidden="true">
            <rect x="1" y="3" width="16" height="11" rx="1" fill="var(--gold-light)"/>
            <path d="M1.5 3.5 L9 9 L16.5 3.5" fill="none" stroke="#fff" stroke-width="1.4"/>
          </svg>
          marisolqtrhomes@brindlemail.com
        </li>
      </ul>
    </div>

    <div class="brokerage">HALVORSEN REALTY</div>
  </section>
</main>
</body>
</html>
```